Menu: A4 (double sided) Lunch/Dinner Menu (one side) + Pizza Menu (other side)

Hello.
We would like to create a new style of menus.
Must be easy to read - a summer feel, crisp, clean, beachy, possible retro feel, colours probably based on our website colours (see address below).
Simple and casual is best as we are a casual beachside Cafe.
This menu will be double sided therefore this job is 2 pages.
If you win this job we will have 2 or 3 more menus for you to create soon after (Drinks, Breakfast, possibly a small Kids menu).
The paper for these menus we expect will be a nice white paper which will then be matte laminated.
Colours possible are the green colour #3a6066, the terracotta on our website logo border and website buttons, maybe a little yellow but must be easy to read on white paper.
Black for text might be okay if this is your best design option.
Please view our website and take a feel for the business, location, the existing website branding and website colours we are trying to achieve, www.saltwrencafe.com.au
We prefer to avoid overwhelming the guest with too many colours on the menus (hence the white paper) as the building is so colourful (La Boca, Argentina, inspired) and the guest experience can be complimented via crisp easy to read menus.
IMPORTANT:
The menus provided please must be fully and easily editable by us in the future.
If you win the job, you must please provide clear instructions on how our staff can edit the menus in the future if project is delivered in Adobe format. Word is also an option for us if you like.
As such, we have attached some documents: the 2x Word documents for the text, 2x .pdf so you can see the fonts and style we were using previously (was printing on recycled brown paper then matte laminated).
If you wished to use the SeaLife Font (this is the existing Font for headings) please let us know as we purchased that font and can provide it.
We have also attached a menu from Quillmont Hotel which we feel has a nice retro feel.
Please include our Instagram in 1 place on the menu @saltwrencafe
Finally, please note,
we never wish to waste anyone's time so we will narrow down the submissions quickly based on first drafts (please know this is because we appreciate your effort and know your time is valuable) and we will then work with the top designer to finalise in a professional fashion.
Thank you.

```html
<!DOCTYPE html>
<html lang="en">
<head>
<meta charset="utf-8">
<title>Salt Wren Cafe menu – A4 double sided</title>
<link href="https://fonts.googleapis.com/css2?family=Bungee+Inline&family=Pacifico&family=Poppins:ital,wght@0,400;0,500;0,700;1,400;1,500&display=swap" rel="stylesheet">
<style>
:root{
  --backdrop:#f1f1ef;
  --paper:#ffffff;
  --ink:#1e1e1e;
  --sea:#2f5a60;
  --veg:#d22c2c;
  --gfo:#1e6db0;
  --extra:#c0652a;
  --wave:#ecedec;
  --caption:#2f5a60;
}
*{box-sizing:border-box;margin:0;padding:0}
html,body{width:1200px;height:850px;overflow:hidden;background:var(--backdrop)}
body{position:relative;font-family:"Poppins",sans-serif;color:var(--ink)}
.page{position:absolute;top:60px;width:506px;height:715px;background:var(--paper);box-shadow:4px 5px 10px rgba(0,0,0,.22)}
.page--food{left:77px}
.page--pizza{left:619px}
.wave-band{position:absolute;background:var(--wave)}
.wave-band--tl{left:0;top:25px;width:77px;height:51px}
.wave-band--tr{right:0;top:25px;width:81px;height:51px}
.wave-band--foot{left:0;right:0;top:648px;height:48px}
.page-title{position:absolute;top:30px;left:0;right:0;text-align:center;font-family:"Bungee Inline",sans-serif;font-size:30px;letter-spacing:2px;line-height:1;white-space:nowrap}
.page--pizza .page-title{left:140px;right:auto;font-size:29px;letter-spacing:1px}
.title-note{position:absolute;left:262px;top:43px;font-size:7.5px;line-height:9px;white-space:nowrap}
.title-note b{font-size:10px}
.legend{position:absolute;top:80px;left:0;right:0;text-align:center;font-size:6px}
.legend .sep{color:#888;margin:0 8px}
.v{color:var(--veg);font-weight:700;font-size:6.4px}
.gfo{color:var(--gfo);font-weight:700;font-size:5.6px}
.plus{color:var(--extra)}
.section-head{position:absolute;left:77px;width:351px;display:flex;align-items:center;gap:10px}
.section-head::before,.section-head::after{content:"";flex:1;height:4px;border-top:2px solid var(--sea);border-bottom:1px solid var(--sea)}
.section-head span{font-family:"Pacifico",cursive;font-weight:400;color:var(--sea);font-size:15px;line-height:1.2}
.col{position:absolute;width:164px}
.col--a{left:76px}
.col--b{left:264px}
.item{margin-bottom:6.5px;font-size:7.2px;line-height:9.3px}
.item-head{display:flex;justify-content:space-between;align-items:baseline}
.item-name{font-weight:700;text-transform:uppercase}
.item-name .qty{font-weight:400}
.item-desc{font-weight:400}
.add{color:var(--extra);font-style:italic;font-size:6.8px}
.add small{font-size:5.6px;font-style:normal;letter-spacing:.3px}
.chili{display:inline-block;width:4px;height:7px;background:var(--veg);border-radius:0 0 4px 1px;transform:rotate(25deg);margin-left:2px;vertical-align:-1px}
.mild{font-size:5.4px;font-style:italic}
.platter{position:absolute;left:77px;top:413px;width:351px;height:67px;border-top:1.5px dotted var(--sea);border-bottom:1.5px dotted var(--sea);border-left:1px solid #9aa9ab;border-right:1px solid #9aa9ab;display:flex}
.platter-text{flex:1;padding:14px 18px 0 17px;font-size:7px;line-height:8.6px;border-right:1px solid #9aa9ab}
.platter-text h3{font-size:10.5px;font-weight:700;line-height:12px;margin-bottom:1px}
.platter-text h3 span{font-weight:500}
.platter-price{width:60px;text-align:center;padding-top:13px}
.platter-price strong{display:block;font-size:16px;font-weight:500}
.platter-price em{font-size:7px;color:var(--extra)}
.sides{position:absolute;left:76px;top:120px;width:351px;height:59px;border-top:1.5px dotted var(--sea);border-bottom:1.5px dotted var(--sea);border-left:1px solid #9aa9ab;display:flex}
.side{flex:1;border-right:1px solid #9aa9ab;text-align:center;padding-top:17px;font-size:7.2px;line-height:10px}
.side b{display:block}
.allergy{position:absolute;left:70px;right:70px;top:663px;text-align:center;font-size:5.6px;line-height:7.3px;font-style:italic}
.allergy strong{color:var(--veg)}
.side-note{position:absolute;left:486px;writing-mode:vertical-rl;transform:rotate(180deg);font-size:6.5px;color:#555;white-space:nowrap}
.side-note--web{top:530px}
.side-note--social{top:457px;font-weight:500}
.side-note--social i{display:inline-block;width:6px;height:6px;border-radius:50%;background:#555;margin-bottom:3px}
.side-note--phone{top:460px}
.side-note--address{top:522px}
.caption{position:absolute;top:798px;left:0;right:0;text-align:center;font-size:17px;color:var(--caption);font-weight:400}
</style>
</head>
<body>

<section class="page page--food">
  <div class="wave-band wave-band--tl" role="img" aria-label="Soft wave pattern band"></div>
  <div class="wave-band wave-band--tr" role="img" aria-label="Soft wave pattern band"></div>
  <h1 class="page-title">LUNCH + DINNER</h1>
  <p class="legend"><span class="v">V</span> Vegetarian<span class="sep">//</span><span class="gfo">GFO</span> Gluten Friendly Optional, please ask</p>

  <h2 class="section-head" style="top:113px"><span>Entree</span></h2>
  <div class="col col--a" style="top:145px">
    <div class="item"><div class="item-head"><span class="item-name">Garlic Bread <span class="qty">(2)</span> <span class="v">V</span></span><span>8</span></div></div>
    <div class="item"><div class="item-head"><span class="item-name">Salt &amp; Pepper Squid</span><span>18</span></div><div class="item-desc">&nbsp;w/ thai dipping sauce</div></div>
    <div class="item"><div class="item-head"><span><span class="item-name">Duo of Dip</span> <span class="v">V</span> w/ pita</span><span>14</span></div></div>
    <div class="item"><div class="item-head"><span><span class="item-name">Bowl of Chips</span> <span class="v">V</span> w/ tomato sauce</span><span>11</span></div></div>
    <div class="item"><div class="item-head"><span class="item-name">Seasoned Wedges <span class="v">V</span></span><span>15</span></div><div class="item-desc">w/ sour cream &amp; sweet chilli 15</div></div>
  </div>
  <div class="col col--b" style="top:145px">
    <div class="item"><div class="item-head"><span class="item-name">Onion Rings <span class="qty">(12)</span> <span class="v">V</span></span><span>13</span></div><div class="item-desc">beer battered w/ tangy mayo</div></div>
    <div class="item"><div class="item-head"><span class="item-name">Vietnamese Spring Rolls <span class="qty">(3)</span></span><span>11</span></div><div class="item-desc">chicken, home-made</div></div>
    <div class="item"><div class="item-head"><span class="item-name">Bruschetta <span class="qty">(1)</span> <span class="v">V</span></span><span>10</span></div><div class="item-desc">w/ olive oil, tomato &amp; red onion salsa, balsamic glaze, feta</div></div>
  </div>

  <h2 class="section-head" style="top:253px"><span>Mains</span></h2>
  <div class="col col--a" style="top:284px">
    <div class="item"><div class="item-head"><span class="item-name">Fish n Chips</span><span>25</span></div><div class="item-desc">house-crumbed butterfish w/ chips, tartare &amp; side salad</div></div>
    <div class="item"><div class="item-head"><span class="item-name">Smokey Beef and Bacon Cheese</span><span>23</span></div><div class="item-desc">Burger w/ chips, onion rings, gerkins &amp; tangy mayo</div><div class="add"><small>ADD</small> jalapenos +2 &nbsp;&nbsp; <small>ADD</small> pineapple +2</div></div>
    <div class="item"><div class="item-head"><span class="item-name">Salt and Pepper Squid</span><span>31</span></div><div class="item-desc">golden tangles w/ chips, thai dipping sauce &amp; side salad</div></div>
  </div>
  <div class="col col--b" style="top:284px">
    <div class="item"><div class="item-head"><span class="item-name">Seafood Basket</span><span>31</span></div><div class="item-desc">crumbed butterfish, grilled prawns, salt &amp; pepper squid, chips, tartare &amp; side salad</div></div>
    <div class="item"><div class="item-head"><span class="item-name">Atlantic Salmon</span><span>31</span></div><div class="item-desc">served w/ mash, teriyaki sauce &amp; winter vegetables <i style="font-weight:500">(contains breadcrumbs)</i></div></div>
    <div class="item"><div class="item-head"><span class="item-name">Chicken Parmigiana</span><span>27</span></div><div class="item-desc">house-crumbed breast schnitzel, napoli sauce, mozzarella, chips &amp; side salad</div><div class="add"><small>ADD</small> bacon and pineapple +4</div><div class="add"><small>ADD</small> jalapenos and pineapple +4</div></div>
  </div>

  <div class="platter">
    <div class="platter-text"><h3>SALT WREN PLATTER <span>for 2</span></h3>beer battered flathead, salt &amp; pepper squid, prawn skewers, grilled chicken, lamb &amp; chorizo, served with antipasto, dipping sauces, pita &amp; garlic bread</div>
    <div class="platter-price"><strong>90</strong><em>(+45 pp)</em></div>
  </div>

  <div class="col col--a" style="top:497px">
    <div class="item"><div class="item-head"><span class="item-name">New York Sirloin <span class="gfo">GFO</span></span><span>38</span></div><div class="item-desc">400g MSA w/ mash &amp; winter vegetables choose: mushroom gravy or classic gravy</div><div class="add"><small>OR</small> surf ‘n’ turf <span class="gfo">GFO</span> +6</div><div class="item-desc"><i>Please allow 35+ minutes for “well-done”</i></div></div>
    <div class="item"><div class="item-head"><span class="item-name">Chicken Caesar</span><span>27</span></div><div class="item-desc">w/ bacon, anchovies, egg, caesar dressing, parmesan, spanish onion, garlic bread</div></div>
    <div class="item"><div class="item-head"><span class="item-name">Lamb Salad <span class="gfo">GFO</span></span><span>30</span></div><div class="item-desc">skewers w/ traditional greek salad, tzatziki &amp; garlic bread &nbsp;&nbsp;&nbsp;&nbsp;&nbsp; <span class="add">extra lamb +8</span></div></div>
  </div>
  <div class="col col--b" style="top:497px">
    <div class="item"><div class="item-head"><span class="item-name">Thai Chicken Curry <span class="chili"></span><span class="mild">MILD</span> <span class="gfo">GFO</span></span><span>26</span></div><div class="item-desc">traditional recipe, w/ jasmine rice &amp; papadums</div></div>
    <div class="item"><div class="item-head"><span class="item-name">Beach Burger <span class="v">V</span></span><span>23</span></div><div class="item-desc">house-made pea &amp; corn ricotta fritter, pineapple, w/ wedges, onion rings, sweet chilli</div></div>
    <div class="item"><div class="item-head"><span class="item-name">Vegan Curry <span class="chili"></span><span class="mild">MILD</span> <span class="gfo">GFO</span> <span class="v">V</span></span><span>24</span></div><div class="item-desc">chickpea &amp; pumpkin w/ fresh tomatoes &amp; basil, jasmine rice &amp; papadums</div></div>
  </div>

  <p class="side-note side-note--social"><i></i> saltwrencafe</p>
  <p class="side-note side-note--web">www.saltwrencafe.com.au</p>

  <div class="wave-band wave-band--foot" role="img" aria-label="Soft wave pattern band"></div>
  <p class="allergy"><strong>Allergies? Please let us know!</strong> All care is taken to cater for allergies including gluten, however our kitchen is small and we do not have separate preparation or cooking areas. As such, there is risk of cross-contact with your allergen and we are unable to guarantee allergen-free meals. Olives may very rarely contain pips.</p>
</section>

<section class="page page--pizza">
  <div class="wave-band wave-band--tl" role="img" aria-label="Soft wave pattern band"></div>
  <div class="wave-band wave-band--tr" role="img" aria-label="Soft wave pattern band"></div>
  <h1 class="page-title">PIZZA</h1>
  <p class="title-note">all <b>12”</b> with house-made<br>tomato base &amp; mozzarella</p>
  <p class="legend"><span class="v">V</span> Vegetarian<span class="sep">//</span>Gluten Free base <span class="plus">+4</span><span class="sep">//</span>Vegan Cheese <span class="plus">+3</span></p>

  <div class="sides">
    <div class="side"><b>GARLIC BREAD</b>8</div>
    <div class="side"><b>GREEK SALAD</b>16</div>
    <div class="side"><b>GARDEN SALAD</b>12</div>
  </div>

  <h2 class="section-head" style="top:203px;left:76px"><span>Standard</span></h2>
  <div class="col col--a" style="top:235px">
    <div class="item"><div class="item-head"><span class="item-name">Hawaiian</span><span>22</span></div><div class="item-desc">ham, pineapple</div></div>
    <div class="item"><div class="item-head"><span class="item-name">Margherita <span class="v">V</span></span><span>22</span></div><div class="item-desc">marinated &amp; diced tomatoes, fresh basil</div></div>
    <div class="item"><div class="item-head"><span class="item-name">BBQ Chicken</span><span>26</span></div><div class="item-desc">chicken, salami, tomato, spanish onion, bbq sauce</div></div>
    <div class="item"><div class="item-head"><span class="item-name">Chorizo <span class="chili"></span></span><span>26</span></div><div class="item-desc">chorizo, salami, tomato, mushrooms, spanish onion</div></div>
    <div class="item"><div class="item-head"><span class="item-name">Salt Wren Special</span><span>26</span></div><div class="item-desc">ham, salami, prawns, kalamata olives, roasted capsicum, mushrooms, spanish onion</div></div>
    <div class="item"><div class="item-head"><span class="item-name">Meat Lovers</span><span>26</span></div><div class="item-desc">chicken, bacon, salami, ham, bbq sauce</div></div>
  </div>
  <div class="col col--b" style="top:235px">
    <div class="item"><div class="item-head"><span class="item-name">Mona Lisa</span><span>26</span></div><div class="item-desc">chicken, pineapple, ham, spanish onion, mushrooms</div></div>
    <div class="item"><div class="item-head"><span class="item-name">Puttanesca</span><span>26</span></div><div class="item-desc">anchovies, capers, salami, kalamata olives, roasted capsicum, parmesan</div></div>
    <div class="item"><div class="item-head"><span class="item-name">Tropical Chicken <span class="chili"></span></span><span>26</span></div><div class="item-desc">chicken, pineapple, spanish onion, chilli, tomato, mushrooms</div></div>
    <div class="item"><div class="item-head"><span class="item-name">Vegetarian <span class="v">V</span></span><span>26</span></div><div class="item-desc">roasted capsicum, tomato, mushrooms, artichokes, kalamata olives, spanish onion</div></div>
    <div class="item"><div class="item-head"><span class="item-name">Build Your Own <span class="v">V</span></span><span>26</span></div><div class="item-desc">tomato base, mozzarella &amp; four toppings</div></div>
  </div>

  <h2 class="section-head" style="top:450px;left:76px"><span>Gourmet</span></h2>
  <div class="col col--a" style="top:482px">
    <div class="item"><div class="item-head"><span class="item-name">Caveman</span><span>29</span></div><div class="item-desc">chicken, lamb, pork sausage, chorizo, salami, bacon, spanish onion, caramelised onion, smokey bbq sauce</div></div>
    <div class="item"><div class="item-head"><span class="item-name">Spicy Prawn &amp; Basil Pesto <span class="chili"></span></span><span>29</span></div><div class="item-desc">prawns, roasted capsicum, chilli, spring onion, basil pesto</div></div>
    <div class="item"><div class="item-head"><span class="item-name">Gourmet Vegetarian <span class="v">V</span></span><span>29</span></div><div class="item-desc">pumpkin, eggplant, semi-dried tomatoes, roasted capsicum, red onion, bulgarian feta, kalamata olives, spinach</div></div>
  </div>
  <div class="col col--b" style="top:482px">
    <div class="item"><div class="item-head"><span class="item-name">Johnny Flash <span class="chili"></span><span class="chili"></span></span><span>29</span></div><div class="item-desc">chilli jam, jalapeno peppers, mushrooms, bacon, chilli, chorizo, spanish onion</div></div>
    <div class="item"><div class="item-head"><span class="item-name">Lamb Pizza</span><span>29</span></div><div class="item-desc">lamb, red onion, fresh tomato, tzatziki, spring onion</div></div>
    <div class="item"><div class="item-head"><span class="item-name">Los Pollos</span><span>29</span></div><div class="item-desc">chicken, pumpkin, basil pesto, spinach, feta, pine nuts</div></div>
    <div class="item"><div class="item-head"><span class="item-name">Seafood Pizza</span><span>29</span></div><div class="item-desc">array of seafood</div></div>
  </div>

  <p class="side-note side-note--phone">PH 8390 1257</p>
  <p class="side-note side-note--address">18 Shoreline Parade Kestrel Bay SA 5172</p>

  <div class="wave-band wave-band--foot" role="img" aria-label="Soft wave pattern band"></div>
  <p class="allergy"><strong>Allergies? Please let us know!</strong> All care is taken to cater for allergies including gluten, however our kitchen is small and we do not have separate preparation or cooking areas. As such, there is risk of cross-contact with your allergen and we are unable to guarantee allergen-free meals. Olives may very rarely contain pips.</p>
</section>

<p class="caption">Salt Wren Cafe menu - A4 double sided</p>
</body>
</html>
```